Stationery design bilingual preschool
Meadowlark preschool
Stationery design bilingual preschool - Childcare
Creative Brief
Bright & Fun-filled
Marita Sundqvist
Preschool director
Lövhagsvägen 9 128 31 Skarpnäck Sweden
angsfagelforskolan@postlada.se
www.angsfagelforskolan.com
Back of the business card suppose to have the same information as the front side but on Swedish.
(Subtitle) Ängsfågel Förskola AB ( name) Marita Sundqvist (title) Förskolechef (address) Lövhagsvägen 9 128 31 Skarpnäck (phone) Tel. 08 731 94 62 (cell) Mob. 073 862 40 15 (email) angsfagelforskolan@postlada.com (web side) www.angsfagelforskolan. com
butterfly2004 butterfly2004
Dear designers, I'd like to see design drafts ideas for the following products: 1. Business card 2. Letterhead 3. Envelope 4. Folder 5. CD and CD cover 6. Email signature 7. Presentation 8.Thank you card 8. Stamp 9. T-shirt, Hoody, Winter jacket/ Rain jacket, Cap, Scarf 10. Pen 11. Meadowlark character toy Thank you, PH

```html
<!DOCTYPE html>
<html lang="en">
<head>
<meta charset="utf-8">
<title>Meadowlark preschool – business card</title>
<link rel="stylesheet" href="https://fonts.googleapis.com/css2?family=Arimo:wght@400;700&display=swap">
<style>
  :root {
    --backdrop: #e9e9e7;
    --card: #ffffff;
    --green: #3aa31f;
    --orange: #f39a12;
    --violet: #8a4bbf;
    --ink: #333333;
    --rule: #9a9a9a;
  }
  * { margin: 0; padding: 0; box-sizing: border-box; }
  html, body {
    width: 1200px; height: 780px; overflow: hidden;
    background: var(--backdrop);
    font-family: "Arimo", Arial, sans-serif;
    color: var(--ink);
  }
  .canvas {
    width: 1200px; height: 780px;
    display: flex; align-items: center; justify-content: center;
  }
  .business-card {
    position: relative;
    width: 900px; height: 500px;
    background: var(--card);
    border-radius: 28px;
    overflow: hidden;
    box-shadow: 0 6px 24px rgba(0,0,0,0.12);
  }
  .edge-bands { position: absolute; inset: 0; width: 100%; height: 100%; }

  .brand {
    position: absolute; top: 110px; left: 0; right: 0;
    display: flex; justify-content: center; align-items: center; gap: 18px;
  }
  .brand-name {
    font-size: 52px; font-weight: 700; color: var(--green);
    letter-spacing: -0.5px; white-space: nowrap;
  }
  .brand-dot {
    width: 56px; height: 56px; border-radius: 50%;
    background: var(--violet); flex: none;
  }

  .details {
    position: absolute; top: 300px; left: 0; right: 0;
    display: flex; justify-content: center;
  }
  .person {
    width: 340px; padding-right: 26px;
    text-align: right;
  }
  .person-name { font-size: 27px; font-weight: 700; color: var(--green); }
  .person-title { margin-top: 8px; font-size: 18px; font-weight: 700; color: var(--orange); }
  .person-address { margin-top: 16px; font-size: 18px; line-height: 1.5; font-style: normal; }

  .divider { width: 1px; background: var(--rule); height: 132px; }

  .contact-list {
    list-style: none; width: 360px; padding-left: 22px;
  }
  .contact-list li {
    display: flex; align-items: center; gap: 12px;
    font-size: 17px; height: 33px; white-space: nowrap;
  }
  .contact-list svg { width: 18px; height: 18px; flex: none; fill: var(--green); }
</style>
</head>
<body>
<main class="canvas">
  <article class="business-card">
    <svg class="edge-bands" viewBox="0 0 900 500" preserveAspectRatio="none" aria-hidden="true">
      <path d="M0 0 H58 C20 140 20 360 58 500 H0 Z" fill="var(--green)"/>
      <path d="M58 0 C20 140 20 360 58 500 L70 500 C30 360 30 140 70 0 Z" fill="var(--orange)"/>
      <path d="M900 0 H842 C880 140 880 360 842 500 H900 Z" fill="var(--green)"/>
      <path d="M842 0 C880 140 880 360 842 500 L830 500 C870 360 870 140 830 0 Z" fill="var(--orange)"/>
    </svg>

    <header class="brand">
      <span class="brand-name">Meadowlark preschool</span>
      <span class="brand-dot"></span>
    </header>

    <section class="details">
      <div class="person">
        <h1 class="person-name">Marita Sundqvist</h1>
        <p class="person-title">Preschool director</p>
        <address class="person-address">Lövhagsvägen 9<br>128 31 Skarpnäck, Sweden</address>
      </div>
      <div class="divider"></div>
      <ul class="contact-list">
        <li>
          <svg viewBox="0 0 24 24" aria-label="Phone"><path d="M6.6 10.8a15 15 0 0 0 6.6 6.6l2.2-2.2c.3-.3.7-.4 1-.2 1.1.4 2.3.6 3.6.6.6 0 1 .4 1 1V20c0 .6-.4 1-1 1A17 17 0 0 1 3 4c0-.6.4-1 1-1h3.5c.6 0 1 .4 1 1 0 1.3.2 2.5.6 3.6.1.3 0 .7-.2 1z"/></svg>
          +46 8 731 94 62
        </li>
        <li>
          <svg viewBox="0 0 24 24" aria-label="Mobile"><path d="M7 1h10a2 2 0 0 1 2 2v18a2 2 0 0 1-2 2H7a2 2 0 0 1-2-2V3a2 2 0 0 1 2-2zm0 3v14h10V4zm5 15.5a1.2 1.2 0 1 0 0 2.4 1.2 1.2 0 0 0 0-2.4z"/></svg>
          +46 73 862 40 15
        </li>
        <li>
          <svg viewBox="0 0 24 24" aria-label="Email"><path d="M2 5h20v14H2zm2 2v.5l8 5 8-5V7zm0 2.8V17h16V9.8l-8 5z"/></svg>
          angsfagelforskolan@postlada.se
        </li>
        <li>
          <svg viewBox="0 0 24 24" aria-label="Website"><path d="M12 2a10 10 0 1 0 0 20 10 10 0 0 0 0-20zm6.9 6h-3a15 15 0 0 0-1.3-3.9A8 8 0 0 1 18.9 8zM12 4c.8 1.2 1.5 2.5 1.9 4h-3.8c.4-1.5 1.1-2.8 1.9-4zM4.3 14a8 8 0 0 1 0-4h3.4a16 16 0 0 0 0 4zm.8 2h3c.3 1.4.8 2.7 1.3 3.9A8 8 0 0 1 5.1 16zm3-8h-3a8 8 0 0 1 4.3-3.9C8.9 5.3 8.4 6.6 8.1 8zM12 20c-.8-1.2-1.5-2.5-1.9-4h3.8c-.4 1.5-1.1 2.8-1.9 4zm2.3-6H9.7a14 14 0 0 1 0-4h4.6a14 14 0 0 1 0 4zm.3 5.9c.5-1.2 1-2.5 1.3-3.9h3a8 8 0 0 1-4.3 3.9zm1.7-5.9a16 16 0 0 0 0-4h3.4a8 8 0 0 1 0 4z"/></svg>
          www.angsfagelforskolan.com
        </li>
      </ul>
    </section>
  </article>
</main>
</body>
</html>
```